4 Poster Designs required for Nail Salon

We require 4 poster designs that will be displayed inside a shopping centre. Each design should contain our logo and the words "Located next to Tallora" (or similar). Design 1 (MOTHERS DAY) should contain the words "Mothers Day Special" and "$10 gift voucher when you spend over $50". Design 2 (CHRISTMAS) should contain the words "Christmas in July" and "Purchase a set of nails and get a $10 gift voucher". Design 3 (ALL YEAR) should contain the words "New Deluxe Spa Pedicure Service" and the words "Try our new Deluxe Spa Pedicure and get a free nail buff, shape and polish for your fingernails". Design 4 (ALL YEAR 2)should contain high quality nail salon image(s) and the words "Now Open". We like designs that support our image of high quality/fun/clean and safe.
Updates
I will close this early. In 24 hours.
Target Market(s)
Rich mums
Industry/Entity Type
Shopping
Look and feel
Each slider illustrates characteristics of the customer's brand and the style your logo design should communicate.

```html
<!DOCTYPE html>
<html lang="en">
<head>
<meta charset="utf-8">
<title>Christmas In July – Petalia Nail Salon Poster</title>
<link rel="stylesheet" href="https://fonts.googleapis.com/css2?family=Parisienne&family=Roboto:wght@400;700&display=swap">
<style>
  :root {
    --canvas-bg: #ecebe8;
    --poster-bg: #ffffff;
    --ink-dark: #3a3a3c;
    --ink-mid: #4a4a4c;
    --script-pink: #e067a4;
    --brand-pink-deep: #d9489a;
    --brand-pink-light: #ec8fc3;
    --logo-white: #ffffff;
    --photo-pink: #f2a9cf;
    --photo-blush: #f6d3df;
    --photo-skin: #e2a98f;
    --photo-skin-deep: #c88770;
  }
  html, body {
    margin: 0;
    padding: 0;
    width: 1200px;
    height: 1148px;
    overflow: hidden;
    background: var(--canvas-bg);
  }
  .poster {
    position: absolute;
    left: 221px;
    top: 39px;
    width: 758px;
    height: 1070px;
    background: var(--poster-bg);
    box-shadow: 0 4px 18px rgba(0,0,0,0.12);
    overflow: hidden;
  }
  .hero-photo {
    position: absolute;
    left: 8px;
    top: 0;
    width: 750px;
    height: 400px;
    background:
      radial-gradient(ellipse 40% 55% at 22% 35%, var(--photo-pink) 0%, var(--photo-blush) 60%, rgba(255,255,255,0) 100%),
      radial-gradient(ellipse 60% 75% at 72% 45%, var(--photo-skin) 0%, var(--photo-skin-deep) 55%, rgba(255,255,255,0) 100%),
      linear-gradient(180deg, #f7e6ea 0%, #ffffff 100%);
  }
  .title {
    position: absolute;
    left: 0;
    top: 430px;
    width: 100%;
    margin: 0;
    font-family: "Parisienne", cursive;
    font-weight: 400;
    color: var(--script-pink);
    font-size: 116px;
    line-height: 0.95;
  }
  .title .line-one { display: block; padding-left: 170px; }
  .title .line-two { display: block; padding-left: 440px; }
  .offer {
    position: absolute;
    left: 380px;
    top: 716px;
    margin: 0;
    font-family: "Roboto", sans-serif;
    font-weight: 700;
    font-size: 24px;
    line-height: 1.15;
    color: var(--ink-dark);
    text-transform: uppercase;
    letter-spacing: 0.2px;
  }
  .brand-panel {
    position: absolute;
    left: 366px;
    top: 792px;
    width: 382px;
    height: 162px;
    background: linear-gradient(90deg, var(--brand-pink-deep) 0%, var(--brand-pink-light) 100%);
    display: flex;
    align-items: center;
    justify-content: center;
  }
  .brand-name {
    font-family: "Roboto", sans-serif;
    font-weight: 400;
    font-size: 46px;
    color: var(--logo-white);
    letter-spacing: 3px;
  }
  .location {
    position: absolute;
    left: 366px;
    top: 970px;
    width: 382px;
    margin: 0;
    text-align: center;
    font-family: "Roboto", sans-serif;
    font-weight: 400;
    font-size: 15px;
    letter-spacing: 4px;
    color: var(--ink-mid);
    text-transform: uppercase;
  }
  .location strong { font-weight: 700; }
</style>
</head>
<body>
  <main class="poster">
    <div class="hero-photo" role="img" aria-label="Photo of pink lilies and pearls beside two hands with French-manicured nails"></div>
    <h1 class="title"><span class="line-one">Christmas In</span><span class="line-two">July</span></h1>
    <p class="offer">Purchase a set of nails and<br>get a $10 gift voucher</p>
    <div class="brand-panel">
      <span class="brand-name">Petalia Nail Salon</span>
    </div>
    <p class="location">Located next to <strong>Tallora</strong></p>
  </main>
</body>
</html>
```